Tidewater Guest Consulting

I am an independent operator engaged on short/medium term consultancy briefs within the Hotel/Resort sector in the Pacific Area and have a representation in Fiji.

A broad based services is offered and includes:

Development Advisory
Property Management
Sales & Marketing
Holiday Ownership/Timeshare
Resorts/Apartments/Motels/Flashpackers/B&B
Financial & Legal Referrals

Industry/Entity Type

Hotel

Contact Information for Business Card

Business name - TIDEWATER GUEST CONSULTING
My name - Marcus Holt
Address: PO Box 318 Coral Heath 4871 Qld
Phone: Australia: +61 7 55019284 Mobile: 0414093857 (Viber)
Fiji: +679 8230519
Email: marcuswholt@tealnest-mail.com

```html
<!DOCTYPE html>
<html lang="en">
<head>
<meta charset="utf-8">
<title>Tidewater Guest Consulting – Business Card</title>
<link rel="stylesheet" href="https://fonts.googleapis.com/css2?family=Cinzel:wght@400;500&family=Didact+Gothic&display=swap">
<style>
  :root {
    --card-bg: #0b0708;
    --card-glow: #140d0e;
    --silver-light: #f2f2f2;
    --silver-mid: #b9b9b9;
    --silver-dark: #7d7d7d;
    --sheen: rgba(205, 205, 205, 0.10);
    --text-soft: #cfcfcf;
    --text-name: #e4e4e4;
  }
  html, body {
    margin: 0;
    padding: 0;
    width: 1200px;
    height: 741px;
    overflow: hidden;
    background: var(--card-bg);
  }
  .card {
    position: relative;
    width: 1200px;
    height: 741px;
    background: radial-gradient(ellipse at 60% 40%, var(--card-glow) 0%, var(--card-bg) 70%);
    overflow: hidden;
  }
  .sheen {
    position: absolute;
    left: 0;
    top: 0;
    width: 1000px;
    height: 470px;
    background: linear-gradient(152deg, transparent 30%, var(--sheen) 44%, transparent 58%);
  }
  .silver {
    background: linear-gradient(180deg, var(--silver-light) 0%, var(--silver-mid) 55%, var(--silver-dark) 100%);
    -webkit-background-clip: text;
    background-clip: text;
    color: transparent;
  }
  .monogram {
    position: absolute;
    left: 68px;
    top: 74px;
    margin: 0;
    font-family: "Cinzel", serif;
    font-weight: 400;
    font-size: 138px;
    line-height: 1;
    letter-spacing: 2px;
  }
  .company {
    position: absolute;
    right: 86px;
    top: 56px;
    margin: 0;
    font-family: "Cinzel", serif;
    font-weight: 400;
    font-size: 58px;
    line-height: 75px;
    letter-spacing: 3px;
    text-align: right;
  }
  .company span { display: block; }
  .person {
    position: absolute;
    left: 119px;
    top: 398px;
    margin: 0;
    font-family: "Didact Gothic", sans-serif;
    font-weight: 400;
    font-size: 38px;
    letter-spacing: 5px;
    color: var(--text-name);
  }
  .contact {
    position: absolute;
    left: 113px;
    top: 490px;
    margin: 0;
    font-family: "Didact Gothic", sans-serif;
    font-weight: 400;
    font-size: 27px;
    line-height: 32.4px;
    letter-spacing: 2.4px;
    color: var(--text-soft);
    font-style: normal;
  }
  .contact span { display: block; }
</style>
</head>
<body>
<main class="card">
  <div class="sheen" role="img" aria-label="Flowing silver swoosh ornament sweeping across the card"></div>

  <h1 class="monogram silver">TGC</h1>
  <h2 class="company silver">
    <span>Tidewater</span>
    <span>Guest</span>
    <span>Consulting</span>
  </h2>

  <p class="person">Marcus Holt</p>

  <address class="contact">
    <span>PO Box 318 Coral Heath 4871 Qld</span>
    <span>Australia: +61 7 55019284</span>
    <span>Mobile: 0414093857 (Viber)</span>
    <span>Fiji: +679 8230519</span>
    <span>marcuswholt@tealnest-mail.com</span>
  </address>
</main>
</body>
</html>
```